360degree attack angle on military vehicle

I need a grahical design/picture, that shows a military vehicle is protected against bullets 360degree around the vehicle and from 0-30degree in elevation.
It needs to have a technical expression, because it will be used by engineers to present the protection of our products.

I have attached a picture that can be used for inspiration.
If a vehicle could be placed in the circle, and the same vehicle transparent rotated around the center. (like the shoe in the picture, but seen from an angle above like the sketch indicates)

Requirements
Must have
• military vehicle

```html
<!DOCTYPE html>
<html lang="en">
<head>
<meta charset="utf-8">
<title>360° Protection</title>
<link href="https://fonts.googleapis.com/css2?family=Krona+One&display=swap" rel="stylesheet">
<style>
  :root {
    --bg-deep: #001a52;
    --bg-mid: #043a8a;
    --bg-glow: #0a4aa0;
    --platform: #1a4f9a;
    --platform-edge: #3a6fb8;
    --cone-top: #0a56b0;
    --cone-side: #7fa7d8;
    --line: #ffffff;
    --text: #ffffff;
    --text-shadow: #7d9fd4;
    --vehicle-dark: #1f2f63;
    --vehicle-mid: #3b4f86;
    --vehicle-light: #9fb4d9;
  }
  html, body {
    margin: 0;
    padding: 0;
    overflow: hidden;
  }
  body {
    width: 1200px;
    height: 960px;
    background: radial-gradient(ellipse 70% 65% at 50% 52%, var(--bg-glow) 0%, var(--bg-mid) 45%, var(--bg-deep) 100%);
  }
  .stage {
    display: block;
    width: 1200px;
    height: 960px;
  }
  .headline,
  .angle-label {
    font-family: "Krona One", sans-serif;
    font-weight: 400;
  }
</style>
</head>
<body>
<svg class="stage" viewBox="0 0 1200 960" xmlns="http://www.w3.org/2000/svg">
  <defs>
    <linearGradient id="cone-side" x1="0" y1="0" x2="1" y2="0">
      <stop offset="0" stop-color="var(--cone-side)" stop-opacity="0.75"/>
      <stop offset="0.5" stop-color="var(--cone-side)" stop-opacity="0.35"/>
      <stop offset="1" stop-color="var(--cone-side)" stop-opacity="0.7"/>
    </linearGradient>
    <linearGradient id="cone-floor" x1="0" y1="0" x2="1" y2="0">
      <stop offset="0" stop-color="#1d5fb5"/>
      <stop offset="0.35" stop-color="#8fb3e0"/>
      <stop offset="0.6" stop-color="#0a4ea6"/>
      <stop offset="1" stop-color="#5d8fd0"/>
    </linearGradient>
    <radialGradient id="vehicle-fill" cx="0.45" cy="0.35" r="0.75">
      <stop offset="0" stop-color="var(--vehicle-light)" stop-opacity="0.85"/>
      <stop offset="0.45" stop-color="var(--vehicle-mid)" stop-opacity="0.85"/>
      <stop offset="1" stop-color="var(--vehicle-dark)" stop-opacity="0.6"/>
    </radialGradient>
    <path id="headline-curve" d="M 215 742 Q 600 800 995 706"/>
  </defs>

  <!-- platform -->
  <g class="platform">
    <ellipse class="platform-glow" cx="600" cy="622" rx="455" ry="178" fill="#ffffff" fill-opacity="0.06"/>
    <ellipse class="platform-ring-outer" cx="597" cy="566" rx="441" ry="106" fill="var(--platform)"/>
    <ellipse class="platform-ring-track" cx="597" cy="575" rx="420" ry="98" fill="none" stroke="var(--platform-edge)" stroke-width="18" stroke-opacity="0.7"/>
    <ellipse class="platform-ring-inner" cx="597" cy="560" rx="405" ry="80" fill="#0b3f88"/>
  </g>

  <!-- protection cone -->
  <g class="protection-cone">
    <ellipse class="cone-floor" cx="597" cy="553" rx="397" ry="68" fill="url(#cone-floor)" fill-opacity="0.85"/>
    <path class="cone-side" d="M 356 220 L 838 220 L 994 553 A 397 68 0 0 1 200 553 Z" fill="url(#cone-side)"/>
    <ellipse class="cone-top" cx="597" cy="220" rx="243" ry="25" fill="var(--cone-top)"/>
    <ellipse class="cone-top-rim" cx="597" cy="222" rx="243" ry="25" fill="none" stroke="#b9d0ef" stroke-opacity="0.5" stroke-width="2"/>
  </g>

  <!-- vehicle illustration area -->
  <rect class="vehicle-illustration" role="img" aria-label="Technical line drawing of an armoured military utility vehicle with roof-mounted gun, shown with transparent rotated copies around the centre" x="300" y="318" width="596" height="266" rx="30" fill="url(#vehicle-fill)"/>

  <!-- elevation angle marker -->
  <g class="angle-marker" stroke="var(--line)" stroke-width="2" fill="none">
    <line x1="146" y1="542" x2="300" y2="539"/>
    <line x1="305" y1="154" x2="431" y2="318"/>
    <path d="M 174 540 Q 175 440 207 367"/>
    <path d="M 247 293 Q 285 238 336 198"/>
  </g>
  <g class="angle-label">
    <text x="179" y="352" font-size="46" fill="var(--text-shadow)">30<tspan font-size="20" dy="-22">°</tspan></text>
    <text x="175" y="348" font-size="46" fill="var(--text)">30<tspan font-size="20" dy="-22">°</tspan></text>
  </g>

  <!-- headline -->
  <text class="headline headline-shadow" fill="var(--text-shadow)" transform="translate(7 7)">
    <textPath href="#headline-curve"><tspan font-size="80">360</tspan><tspan font-size="30" dy="-40">°</tspan><tspan font-size="54" dy="40"> PROTECTION</tspan></textPath>
  </text>
  <text class="headline" fill="var(--text)">
    <textPath href="#headline-curve"><tspan font-size="80">360</tspan><tspan font-size="30" dy="-40">°</tspan><tspan font-size="54" dy="40"> PROTECTION</tspan></textPath>
  </text>
</svg>
</body>
</html>
```